Coffee pack for specialty coffee roasters

Tres Lunas is a premium brand of specialty coffee roasters based in Prague in the Czech Republic.
We sell coffee beans to other coffee shops (wholesale channel) or to final consumers in our own coffee shops (retail)
We are roasting only specialty grade coffee that we source either directly or through specialty coffee merchants.
We have usually 6-8 coffees on our offer list. Each coffee stays with us 2-7 months based on their harvest season.
We pack our coffee for retail purposes in 250g bags that we sell in our cafés, roastery and clients.
We are now changing our bags from side gusset bags with valve closed by tin ties to flat bottom bags with zipper and valve.
We want evolution of our packaging design (not revolution)
Our current bags are decorated by front and back stickers.
New bags will be custom printed with general information and logo (e.g. Manufacturer information, contact, size etc.) and we want to have paper sleeve with customizable information (e.g. Name of the Coffee origin, farmer, taste profile, farm info etc.)

Target Market(s)

Men + woman aged 25-45, socioeconomical group A and B, university educated, interested in quality products, they care about what they drink and eat.

Industry/Entity Type

Coffee Shop

Font styles to use
Other font styles liked:
• Platform regular

Requirements
Must have
• Design of the pack itself and design of paper sleeve that will be excheangable (we need to change name of the coffee and information about it on the paper sleeve)
Nice to have
• nice to have- coffee related design on the bag under the sleeve
Should not have
• any crazy colours (the bag is golden with only black print on it) and sleeve can be colourful but nothing extravagant.

```html
<!DOCTYPE html>
<html lang="cs">
<head>
<meta charset="utf-8">
<title>Tres Lunas – obal a rukáv 250 g</title>
<link href="https://fonts.googleapis.com/css2?family=Jost:wght@400;500;600&family=Archivo+Narrow:wght@400;500&display=swap" rel="stylesheet">
<style>
:root{
  --ink:#111;
  --paper:#fff;
  --gold:#e9a23b;
  --sleeve-black:#0b0b0b;
  --roast:#6b3f1d;
  --roast-dark:#3a2210;
  --guide-blue:#3fb6e6;
  --guide-red:#e02a2a;
  --guide-pink:#e0218a;
  --fold:#777;
}
*{box-sizing:border-box;margin:0;padding:0}
html,body{width:1200px;height:877px;overflow:hidden;background:var(--paper)}
body{position:relative;font-family:"Archivo Narrow",Arial,sans-serif;color:var(--ink)}
.abs{position:absolute}
.dim{font-family:"Jost",sans-serif;font-size:7px;color:#333}
.dim-big{font-family:"Jost",sans-serif;font-size:17px;background:var(--paper);padding:0 4px}

/* bag dieline */
.bag-frame{left:26px;top:17px;width:1036px;height:544px;border:1px solid var(--guide-blue)}
.fold-v{width:0;border-left:1px dashed var(--fold)}
.tear{height:0;border-top:1px dashed var(--guide-red);left:209px;width:328px}
.brand{font-family:"Jost",sans-serif;font-weight:500;letter-spacing:.04em;text-align:center;color:var(--ink)}
.brand-mark{border:5px solid var(--ink);border-radius:50%;margin:0 auto}
.illustration-band{left:0;top:351px;width:1083px;height:179px;background:linear-gradient(180deg,#f4f4f4,#c9c9c9 55%,#e6e6e6)}
.open-here{left:743px;top:68px;font-family:"Jost",sans-serif;font-size:8px;font-weight:500;display:flex;align-items:center;gap:6px}
.open-here .dots{width:250px;border-top:4px dotted var(--ink)}
.bag-intro{left:742px;top:139px;width:104px;font-size:7.6px;line-height:1.15}
.maker{right:167px;top:216px;text-align:right;font-size:6.4px;line-height:1.3}
.weight{right:167px;top:275px;font-family:"Jost",sans-serif;font-size:10px}
.weight b{font-size:22px;font-weight:600}

/* sleeve */
.sleeve-frame{left:56px;top:631px;width:1110px;height:215px;border:1px solid var(--guide-blue)}
.sleeve-band{left:50px;top:627px;width:983px;height:223px;background:var(--gold)}
.sleeve-body{left:56px;top:643px;width:977px;height:192px;background:var(--sleeve-black);color:#fff;overflow:hidden}
.map-area{left:153px;top:0;width:133px;height:192px;background:linear-gradient(160deg,#4a2c14,#2a180b)}
.scene-area{left:286px;top:0;width:535px;height:192px;background:linear-gradient(90deg,var(--roast),#7a4a22 50%,var(--roast-dark))}
.sleeve-body .fold-v{top:0;height:192px;border-color:#666}
.story{left:23px;top:22px;width:110px;font-size:7.3px;line-height:1.32;text-align:justify}
.specs{right:697px;top:22px;text-align:right;font-family:"Jost",sans-serif;font-size:10px;line-height:1.3}
.accent-bar{width:3px;background:var(--gold)}
.origin{left:295px;top:14px}
.origin h1{font-family:"Jost",sans-serif;font-weight:400;font-size:38px;line-height:1}
.origin .farm{font-family:"Jost",sans-serif;font-size:16px;margin-top:2px}
.origin .notes{font-family:"Jost",sans-serif;font-size:14px;line-height:1.1;margin-top:18px}
.origin .roasted{font-family:"Jost",sans-serif;font-size:14px;margin-top:12px}
.region{left:192px;top:169px;font-family:"Jost",sans-serif;font-size:10px;letter-spacing:.06em;color:var(--gold)}
.roast-dots{left:288px;top:174px;width:540px;border-top:4px dotted var(--gold)}
.taste-label{font-family:"Jost",sans-serif;font-size:8px;transform:translateX(-50%)}
.recipe-title{right:248px;top:58px;text-align:right;font-family:"Jost",sans-serif;font-size:11px;line-height:1}
.recipe-row{right:172px;text-align:right;font-family:"Jost",sans-serif;font-size:7.6px;line-height:1.2}
.badge{width:34px;height:34px;border-radius:50%;background:#fff;border:3px solid #bbb;color:#111;font-family:"Jost",sans-serif;font-size:7px;font-weight:600;display:flex;align-items:center;justify-content:center;text-align:center;line-height:1}
.profile{left:856px;top:21px;width:122px;font-size:7.6px;line-height:1.3}
.profile h2{font-family:"Jost",sans-serif;font-weight:400;font-size:7.6px;margin-bottom:7px}
.contacts{left:856px;top:156px;font-family:"Jost",sans-serif;font-size:7.8px;line-height:1.45}
.contacts .dot{display:inline-block;width:7px;height:7px;background:#fff;margin-right:3px;vertical-align:-1px}
</style>
</head>
<body>

<!-- bag dieline -->
<div class="abs dim-big" style="left:520px;top:-4px">370mm</div>
<div class="abs bag-frame"></div>
<div class="abs fold-v" style="left:209px;top:17px;height:544px"></div>
<div class="abs fold-v" style="left:542px;top:17px;height:544px"></div>
<div class="abs fold-v" style="left:722px;top:17px;height:544px"></div>

<svg class="abs" style="left:204px;top:17px" width="30" height="46" aria-hidden="true">
  <line x1="7" y1="2" x2="7" y2="42" stroke="#111"/>
  <path d="M3 7 L7 1 L11 7 M3 37 L7 43 L11 37" fill="none" stroke="#111"/>
  <text x="11" y="25" font-size="8" font-family="Jost,sans-serif">15mm</text>
</svg>
<svg class="abs" style="left:532px;top:53px" width="12" height="12" aria-hidden="true"><path d="M10 1 L1 6 L10 11Z" fill="var(--guide-red)"/></svg>
<div class="abs tear" style="top:88px"></div>
<div class="abs tear" style="top:101px"></div>
<div class="abs tear" style="top:114px"></div>

<div class="abs" style="left:265px;top:158px;width:220px">
  <div class="brand-mark" style="width:70px;height:70px"></div>
  <div class="brand" style="font-size:31px;margin-top:30px">TRES LUNAS</div>
</div>

<div class="abs open-here">ZDE OTEVŘÍT <span class="dots"></span>
  <svg width="10" height="10" aria-hidden="true"><path d="M0 1 L9 5 L0 9Z" fill="#111"/></svg></div>
<div class="abs" style="left:889px;top:25px;height:124px;border-left:1px solid var(--guide-pink)"></div>
<div class="abs" style="left:891px;top:84px;font-family:Jost,sans-serif;font-size:9px;color:var(--guide-pink);transform:rotate(-90deg)">50mm</div>

<p class="abs bag-intro">V rukou držíte čerstvě praženou zrnkovou kávu. Jde o výběrovou jednodruhovou arabiku s min. 85 body, která pochází z farem s ručním sběrem. Chceme Vám přinášet to nejlepší z aktuálních sklizní a zároveň podporovat poctivé farmáře. Proto s nimi navazujeme co nejpřímější, často i osobní vztahy. Věříme, že tak si užijí kávu všichni, kdo se na její cestě z plantáže až do šálku podílí.</p>

<div class="abs" style="left:922px;top:140px;width:120px">
  <div class="brand-mark" style="width:40px;height:40px;border-width:3px"></div>
  <div class="brand" style="font-size:16px;margin-top:10px">TRES LUNAS</div>
</div>
<div class="abs maker">Výrobce: Tres Lunas s.r.o.,<br>Korunní 812/44, 120 00, Praha 2, ČR<br><span style="display:block;margin-top:3px">Minimální trvanlivost 90 dní<br>od data pražení uvedeného na obalu</span><span style="display:block;margin-top:3px">Nejlepší chuti dosáhnete do 30 dnů od pražení kávy.</span></div>
<div class="abs weight">Hmotnost: <b>250</b>g</div>

<div class="abs illustration-band" role="img" aria-label="Černobílá kresba kávovníku, sběrače, zrn, mlýnku a šálků kávy"></div>

<div class="abs dim" style="left:22px;top:286px;transform:rotate(-90deg)">195</div>
<div class="abs dim" style="left:1052px;top:280px;font-size:10px;transform:rotate(90deg)">195mm</div>
<div class="abs" style="left:26px;top:560px;width:1036px;border-top:1px solid #999"></div>
<div class="abs dim" style="left:114px;top:559px">65</div>
<div class="abs dim" style="left:370px;top:559px">120</div>
<div class="abs dim" style="left:627px;top:559px">65</div>
<div class="abs dim" style="left:884px;top:559px">120</div>

<!-- sleeve -->
<div class="abs" style="left:56px;top:618px;width:1110px;border-top:1px solid #999"></div>
<div class="abs dim-big" style="left:538px;top:598px">400mm</div>
<div class="abs sleeve-frame"></div>
<div class="abs sleeve-band"></div>
<div class="abs sleeve-body">
  <div class="abs map-area" role="img" aria-label="Mapa Jižní Ameriky s vyznačenou oblastí původu"></div>
  <div class="abs scene-area" role="img" aria-label="Kresba pěstování a přípravy kávy v hnědých tónech"></div>
  <svg class="abs" style="left:196px;top:107px" width="14" height="14" aria-hidden="true"><circle cx="7" cy="7" r="6" fill="var(--gold)"/></svg>

  <div class="abs fold-v" style="left:153px"></div>
  <div class="abs fold-v" style="left:486px"></div>
  <div class="abs fold-v" style="left:638px"></div>
  <div class="abs fold-v" style="left:796px"></div>

  <p class="abs story">Jsme velmi hrdí, že tato káva se prezentuje v naší pražírně již počtvrté. V ruce držíte čerstvou sklizeň odrůdy caturra a pacas. Tato káva roste ve výšce kolem 1700 metrů nad mořem na svazích sopky Pichincha ve specifické biodiverzní oblasti mezi pralesem a Andami. Sklizeň této kávy probíhala mezi červencem a říjnem 2016 a byla sbírána výhradně ručně. Rok od roku také vidíme zlepšující se třídění a balení kávy. Kvalita je jednoduše hlavní prioritou farmáře Martína Olmeda.</p>

  <div class="abs specs">100%<br>ARABICA CATURRA<br>ZPRACOVÁNÍ:<br>PROMYTÉ</div>
  <div class="abs accent-bar" style="left:284px;top:22px;height:52px"></div>

  <div class="abs origin">
    <h1>Ekvádor</h1>
    <div class="farm">FARMA: LAS BRISAS</div>
    <div class="notes">Lískové ořechy,<br>mléčná čokoláda,<br>karamel</div>
    <div class="roasted">Praženo:</div>
  </div>
  <div class="abs region">PICHINCHA</div>
  <div class="abs roast-dots"></div>

  <svg class="abs" style="left:514px;top:48px" width="90" height="90" viewBox="-45 -45 90 90" aria-label="Chuťový profil">
    <g fill="none" stroke-width="3">
      <polygon points="0,-40 35,-20 35,20 0,40 -35,20 -35,-20" stroke="#fff"/>
      <polygon points="0,-30 26,-15 26,15 0,30 -26,15 -26,-15" stroke="var(--gold)"/>
      <polygon points="0,-20 17,-10 17,10 0,20 -17,10 -17,-10" stroke="#fff"/>
      <polygon points="0,-11 10,-5.5 10,5.5 0,11 -10,5.5 -10,-5.5" stroke="var(--gold)"/>
    </g>
    <text x="0" y="3" fill="#fff" font-size="9" text-anchor="middle" font-family="Jost,sans-serif">6 7 8 9 10</text>
  </svg>
  <span class="abs taste-label" style="left:559px;top:42px">Aroma</span>
  <span class="abs taste-label" style="left:520px;top:61px">Tělo</span>
  <span class="abs taste-label" style="left:608px;top:61px">Kyselost</span>
  <span class="abs taste-label" style="left:513px;top:118px">Dochuť</span>
  <span class="abs taste-label" style="left:606px;top:118px">Horkost</span>
  <span class="abs taste-label" style="left:559px;top:136px">Sladkost</span>

  <div class="abs recipe-title">DOPORUČENÝ<br>RECEPT NA<br>ESPRESSO</div>
  <div class="abs accent-bar" style="left:736px;top:102px;height:123px;top:9px"></div>

  <div class="abs recipe-row" style="top:22px">GRAMÁŽ KÁVY<br>DO PORTAFILTERU</div>
  <div class="abs recipe-row" style="top:64px">CÍLOVÁ<br>HMOTNOST<br>ESPRESSA</div>
  <div class="abs recipe-row" style="top:114px">CELKOVÝ ČAS<br>EXTRAKCE</div>
  <div class="abs badge" style="left:811px;top:11px">18g</div>
  <div class="abs badge" style="left:811px;top:57px">36g</div>
  <div class="abs badge" style="left:811px;top:101px">28<br>sekund</div>

  <div class="abs profile"><h2>CHUŤOVÝ<br>PROJEV ESPRESSA:</h2>Ekvádor je na espressu krásně vybalancovaný s vůní pralinek a medu. V chuti se pak projevuje převážně chuť čokolády a másla s jemnou oříškovou dochutí. Díky tomu se hodí i na přípravu cappuccina a dalších mléčných variací.</div>
  <div class="abs contacts">www.tres-lunas.cz<br><span class="dot"></span>@tlroastery<br><span class="dot"></span>FB/prazirnatreslunas</div>
</div>

<div class="abs dim" style="left:1186px;top:730px;font-size:10px;transform:rotate(90deg)">77mm</div>
<div class="abs" style="left:56px;top:866px;width:1110px;border-top:1px solid #999"></div>
<div class="abs dim" style="left:127px;top:866px">55</div>
<div class="abs dim" style="left:370px;top:866px">120</div>
<div class="abs dim" style="left:614px;top:866px">55</div>
<div class="abs dim" style="left:856px;top:866px">120</div>
<div class="abs dim" style="left:1092px;top:866px">50</div>

</body>
</html>
```